Surgery Office Letterhead Design

I'm seeking new letterhead that will comprise all of our office locations and logo and other applicable information, per the following:

Office Locations:

Lakemont Institute for Jaw & Face Surgery at Marlowe Springs
347 Hazelpine Court
Marlowe Springs, Texas 70012
Phone 817.382.4706
Fax 817.382.9034

Lakemont Institute for Jaw & Face Surgery at Cedarbrook
518 Willowgate Boulevard
Cedarbrook, Texas 70024
Phone 254.563.2781
Fax 254.563.2789

Lakemont Institute for Jaw & Face Surgery at Fallon Ridge
739 West 9th Avenue
Fallon Ridge, Texas 70036
Phone 254.871.4035
Fax 254.871.4042

Other Info to include:

www.lakemontjawface.com
hello@lakemontjawface.com

Industry/Entity Type

Medical

Font styles to use
Serif
Sans Serif

Requirements
Must have
• See Project Description

```html
<!DOCTYPE html>
<html lang="en">
<head>
<meta charset="utf-8">
<title>Lakemont Institute Letterhead</title>
<link href="https://fonts.googleapis.com/css2?family=Libre+Baskerville:wght@700&family=Open+Sans:wght@400;700&display=swap" rel="stylesheet">
<style>
  :root {
    --backdrop: #1ea9d8;
    --paper: #ffffff;
    --navy: #2c4677;
    --navy-light: #5b78aa;
    --ink: #8a8f98;
    --ink-dark: #4a4f58;
    --rule: #d9dde3;
  }
  * { margin: 0; padding: 0; box-sizing: border-box; }
  html, body { width: 1200px; height: 1000px; overflow: hidden; }
  body {
    background: var(--backdrop);
    font-family: "Open Sans", Arial, sans-serif;
    position: relative;
  }
  .letterhead {
    position: absolute;
    left: 250px; top: 47px;
    width: 700px; height: 906px;
    background: var(--paper);
    overflow: hidden;
    box-shadow: 0 12px 30px rgba(0, 40, 70, 0.25);
  }
  .header-wave { position: absolute; left: 0; top: 0; width: 700px; height: 260px; }
  .brand {
    position: absolute; left: 48px; top: 44px;
    display: flex; align-items: center; gap: 10px;
  }
  .brand-mark { width: 22px; height: 22px; border-radius: 50%; background: var(--navy); flex: none; }
  .brand-name {
    font-family: "Libre Baskerville", Georgia, serif;
    font-weight: 700; font-size: 17px; letter-spacing: 1px;
    color: var(--navy); text-transform: uppercase; line-height: 1.2;
  }
  .letter-body {
    position: absolute; left: 48px; top: 150px; width: 470px;
    font-size: 10.5px; line-height: 1.75; color: var(--ink);
  }
  .salutation { color: var(--navy); font-weight: 700; margin-bottom: 40px; }
  .letter-body p + p { margin-top: 16px; }
  .signature {
    position: absolute; left: 48px; top: 560px;
    width: 160px; height: 60px;
    background: linear-gradient(90deg, rgba(59,63,70,0.18), rgba(59,63,70,0.06));
    border-radius: 4px;
  }
  .locations {
    position: absolute; left: 48px; top: 700px; width: 604px;
    display: flex; justify-content: space-between;
  }
  .location {
    width: 186px; padding-left: 10px;
    border-left: 2px solid var(--navy);
    font-size: 9.5px; line-height: 1.55; color: var(--ink);
    font-style: normal;
  }
  .location-name { color: var(--navy); font-weight: 700; margin-bottom: 4px; }
  .contact-line {
    position: absolute; left: 48px; right: 48px; top: 846px;
    padding-top: 6px; border-top: 1px solid var(--navy);
    font-size: 10px; color: var(--navy); letter-spacing: 0.3px;
  }
  .contact-line .divider { margin: 0 8px; }
  .footer-band {
    position: absolute; left: 0; bottom: 0; width: 700px; height: 18px;
    background: var(--navy);
  }
</style>
</head>
<body>
  <main class="letterhead">
    <svg class="header-wave" viewBox="0 0 700 260" aria-hidden="true">
      <path d="M330 0 C430 20 520 70 580 130 C620 170 660 210 700 250 L700 0 Z" fill="var(--navy-light)"/>
      <path d="M350 0 C450 18 535 62 595 118 C632 152 668 188 700 222 L700 0 Z" fill="var(--navy)"/>
    </svg>

    <header class="brand">
      <span class="brand-mark"></span>
      <span class="brand-name">Lakemont Institute<br>for Jaw &amp; Face Surgery</span>
    </header>

    <section class="letter-body">
      <p class="salutation">Dear Sir,</p>
      <p>We are pleased to share this update on the care our surgical team provides across our three Texas offices. Our staff works closely with referring dentists and physicians to plan each treatment with clarity and comfort for every patient we serve.</p>
      <p>From the first consultation through recovery, we explain every step, answer questions openly and keep your records secure. Appointments can be arranged at the office nearest to you, and our coordinators will gladly help with scheduling and insurance details.</p>
      <p>Thank you for the trust you place in our practice. Please contact us by phone or email with any questions, and we look forward to working with you.</p>
    </section>

    <div class="signature" role="img" aria-label="Handwritten signature of the surgeon"></div>

    <section class="locations">
      <address class="location">
        <div class="location-name">Lakemont Institute for Jaw &amp; Face Surgery at Marlowe Springs</div>
        347 Hazelpine Court<br>Marlowe Springs, Texas 70012<br>Phone 817.382.4706<br>Fax 817.382.9034
      </address>
      <address class="location">
        <div class="location-name">Lakemont Institute for Jaw &amp; Face Surgery at Cedarbrook</div>
        518 Willowgate Boulevard<br>Cedarbrook, Texas 70024<br>Phone 254.563.2781<br>Fax 254.563.2789
      </address>
      <address class="location">
        <div class="location-name">Lakemont Institute for Jaw &amp; Face Surgery at Fallon Ridge</div>
        739 West 9th Avenue<br>Fallon Ridge, Texas 70036<br>Phone 254.871.4035<br>Fax 254.871.4042
      </address>
    </section>

    <footer class="contact-line">
      www.lakemontjawface.com<span class="divider">|</span>hello@lakemontjawface.com
    </footer>
    <div class="footer-band"></div>
  </main>
</body>
</html>
```